Gruppo Abitativo Sorena
complete stationary set
Gruppo Abitativo Sorena - Real Estate
Creative Brief
Professional
Marcello Ruffoni
Responsabile di agenzia
Gruppo Abitativo Sorena Via Castellana, 147 20384 Milano - Italy
marcello.ruffoni@gruppoabitativosorena.example
www.gruppoabitativosorena.example
I'm looking for a complete set of stationary: 1. Business Cards 2. Letter Head 3. Presentation Folder 6. Envelopes 7. PowerPoint slide template 9. Note pad cover 10. e-mail signature 11. Fax Cover Please insert QR Code and a photo box in business card. For further information post comments or contact me I will give you all feedback you need
Should have something to that represents our company and will make them want to look at the card again.

```html
<!DOCTYPE html>
<html lang="it">
<head>
<meta charset="utf-8">
<title>Gruppo Abitativo Sorena – Stationery</title>
<link href="https://fonts.googleapis.com/css2?family=Open+Sans:wght@400;600;700&display=swap" rel="stylesheet">
<style>
:root{
  --bg:#e4e5e7;
  --paper:#ffffff;
  --navy:#1b3a78;
  --navy-deep:#0f2553;
  --blue:#2f5fae;
  --grey:#8a8f98;
  --grey-light:#c9ccd1;
  --ink:#333a45;
  --faint:#eef1f6;
}
*{box-sizing:border-box;margin:0;padding:0}
html,body{width:1200px;height:310px;overflow:hidden;background:var(--bg);font-family:"Open Sans",Arial,sans-serif;color:var(--ink)}
.canvas{position:relative;width:1200px;height:310px}
.item{position:absolute;background:var(--paper);box-shadow:0 1px 3px rgba(0,0,0,.25);overflow:hidden}
.label{position:absolute;font-size:6px;color:var(--grey);text-align:center;width:100%;bottom:-10px;left:0}
.wrap{position:absolute}
.brand{display:flex;align-items:center;gap:4px;color:var(--navy);font-weight:700;white-space:nowrap}
.brand .mark{background:var(--navy);flex:none}
.brand.light{color:#fff}
.brand.light .mark{background:#fff}
.wave{position:absolute;left:0;bottom:0;width:100%}
.faint-mark{position:absolute;background:var(--faint)}
.tiny{font-size:4px;line-height:1.5;color:var(--ink)}

/* email signature */
.signature{left:20px;top:18px;width:340px;height:74px}
.signature .brand{font-size:13px}
.signature .brand .mark{width:14px;height:14px}
.signature .name{font-size:8px;font-weight:700;color:var(--navy);margin-top:6px}
.signature .role{font-size:6px;color:var(--grey)}
.signature .contact{position:absolute;left:190px;top:2px;font-size:5.5px;line-height:1.6}
.signature .rule{height:2px;background:linear-gradient(90deg,var(--navy),var(--blue));margin-top:5px;width:180px}

/* cards */
.card{width:140px;height:80px}
.card .brand{font-size:6.5px}
.card .brand .mark{width:7px;height:7px}
.card.dark{background:linear-gradient(160deg,var(--blue),var(--navy-deep))}
.photo{position:absolute;background:linear-gradient(135deg,#b9c4d6,#7d8ca5)}
.qr{position:absolute;background:var(--grey-light)}

/* letterheads */
.letterhead{width:170px;height:240px;top:18px}
.letterhead .brand{font-size:8px}
.letterhead .brand .mark{width:9px;height:9px}

/* slips */
.slip{width:200px;height:95px;left:760px}
.slip .brand{font-size:7px}
.slip .brand .mark{width:8px;height:8px}

/* envelopes */
.envelope{width:195px;height:70px;left:985px}
.envelope.back{background:linear-gradient(#d3d5d9,#bfc2c7)}
.envelope .brand{font-size:6px}
.envelope .brand .mark{width:7px;height:7px}
.window{position:absolute;border:1px solid var(--grey-light);background:#f7f8fa}
</style>
</head>
<body>
<div class="canvas">

  <!-- email signature -->
  <section class="wrap signature">
    <div class="brand"><span class="mark"></span>Gruppo Abitativo Sorena</div>
    <div class="rule"></div>
    <div class="name">Marcello Ruffoni</div>
    <div class="role">Responsabile di agenzia</div>
    <div class="contact">
      Via Castellana, 147 · 20384 Milano - Italy<br>
      marcello.ruffoni@gruppoabitativosorena.example<br>
      www.gruppoabitativosorena.example
    </div>
  </section>

  <!-- business card front -->
  <article class="item card" style="left:25px;top:122px">
    <div class="brand" style="position:absolute;left:8px;top:8px"><span class="mark"></span>Gruppo Abitativo Sorena</div>
    <div class="tiny" style="position:absolute;left:8px;top:40px">
      <b style="color:var(--navy)">Marcello Ruffoni</b><br>Responsabile di agenzia<br>Via Castellana, 147 · 20384 Milano
    </div>
    <div class="photo" role="img" aria-label="Portrait photo box" style="right:8px;top:22px;width:28px;height:34px"></div>
    <svg class="wave" viewBox="0 0 140 12" height="12" preserveAspectRatio="none"><path d="M0 6 Q70 0 140 6 V12 H0Z" fill="var(--navy)"/></svg>
    <span class="label">Card Front</span>
  </article>

  <!-- business card back -->
  <article class="item card" style="left:185px;top:122px">
    <div class="brand" style="position:absolute;left:8px;top:10px"><span class="mark"></span>Gruppo Abitativo Sorena</div>
    <div class="tiny" style="position:absolute;left:8px;top:40px">marcello.ruffoni@gruppoabitativosorena.example<br>www.gruppoabitativosorena.example</div>
    <div class="qr" role="img" aria-label="QR code area" style="right:8px;top:8px;width:22px;height:22px"></div>
    <svg class="wave" viewBox="0 0 140 12" height="12" preserveAspectRatio="none"><path d="M0 6 Q70 0 140 6 V12 H0Z" fill="var(--navy)"/></svg>
    <span class="label">Card Back</span>
  </article>

  <!-- alt cards -->
  <article class="item card" style="left:25px;top:212px">
    <div class="brand" style="position:absolute;left:8px;top:34px"><span class="mark"></span>Gruppo Abitativo Sorena</div>
    <svg class="wave" viewBox="0 0 140 14" height="14" preserveAspectRatio="none"><path d="M0 8 Q70 0 140 8 V14 H0Z" fill="var(--blue)"/></svg>
    <span class="label">Card Front Alt</span>
  </article>
  <article class="item card dark" style="left:185px;top:212px">
    <div class="brand light" style="position:absolute;left:8px;top:10px"><span class="mark"></span>Gruppo Abitativo Sorena</div>
    <div class="tiny" style="position:absolute;left:8px;top:44px;color:#dfe6f3">Marcello Ruffoni<br>www.gruppoabitativosorena.example</div>
    <span class="label">Card Back Alt</span>
  </article>

  <!-- letterheads -->
  <article class="item letterhead" style="left:380px">
    <div class="brand" style="position:absolute;left:12px;top:12px"><span class="mark"></span>Gruppo Abitativo Sorena</div>
    <div class="faint-mark" style="left:55px;top:85px;width:60px;height:60px"></div>
    <svg class="wave" viewBox="0 0 170 20" height="20" preserveAspectRatio="none"><path d="M0 10 Q85 0 170 10 V20 H0Z" fill="var(--navy)"/><path d="M0 8 Q85 -2 170 8" stroke="var(--blue)" fill="none"/></svg>
    <span class="label">Letterhead Page 1</span>
  </article>
  <article class="item letterhead" style="left:565px">
    <div class="faint-mark" style="left:55px;top:85px;width:60px;height:60px"></div>
    <svg class="wave" viewBox="0 0 170 20" height="20" preserveAspectRatio="none"><path d="M0 10 Q85 0 170 10 V20 H0Z" fill="var(--navy)"/><path d="M0 8 Q85 -2 170 8" stroke="var(--blue)" fill="none"/></svg>
    <span class="label">Letterhead Page 2</span>
  </article>

  <!-- compliment slips -->
  <article class="item slip" style="top:70px">
    <div class="brand" style="position:absolute;left:10px;top:10px"><span class="mark"></span>Gruppo Abitativo Sorena</div>
    <div class="faint-mark" style="right:20px;top:20px;width:40px;height:40px"></div>
    <svg class="wave" viewBox="0 0 200 14" height="14" preserveAspectRatio="none"><path d="M0 7 Q100 0 200 7 V14 H0Z" fill="var(--navy)"/></svg>
    <span class="label">Compliment Slip</span>
  </article>
  <article class="item slip" style="top:178px">
    <div class="brand" style="position:absolute;left:10px;top:10px"><span class="mark"></span>Gruppo Abitativo Sorena</div>
    <svg class="wave" viewBox="0 0 200 14" height="14" preserveAspectRatio="none"><path d="M0 7 Q100 0 200 7 V14 H0Z" fill="var(--navy)"/></svg>
    <span class="label">Compliment Slip</span>
  </article>

  <!-- envelopes -->
  <article class="item envelope back" style="top:48px">
    <svg width="195" height="70" viewBox="0 0 195 70" style="position:absolute;left:0;top:0"><path d="M0 0 L97.5 38 L195 0" fill="#e6e7ea" stroke="#b3b6bc"/></svg>
    <span class="label">Envelope Back</span>
  </article>
  <article class="item envelope" style="top:132px">
    <div class="brand" style="position:absolute;left:10px;top:10px"><span class="mark"></span>Gruppo Abitativo Sorena</div>
    <svg class="wave" viewBox="0 0 195 10" height="10" preserveAspectRatio="none"><path d="M0 5 Q97 0 195 5 V10 H0Z" fill="var(--navy)"/></svg>
    <span class="label">DL Envelope</span>
  </article>
  <article class="item envelope" style="top:216px">
    <div class="brand" style="position:absolute;left:10px;top:10px"><span class="mark"></span>Gruppo Abitativo Sorena</div>
    <div class="window" style="left:20px;top:30px;width:70px;height:22px"></div>
    <span class="label">Window Envelope</span>
  </article>

</div>
</body>
</html>
```